professional looking data specialist website

I've recently had a new logo designed and I'm now looking to get a professional looking website built. This is for a new company that specialises in data. We look to support companies with business intelligence, report modelling, data governance to new european legislation (GDPR). We are offer consultancy or we can attend site and complete work when required. Our target arket is united kingdom wide and we are specifically aiming at small to medium sized companies.

Target Market(s)

small to medium enterprise companies from all industries

Industry/Entity Type

Professional Service

Coding

Coded - Design and coding required

Number of Pages Required

4 page

Font styles to use
Sans Serif

Colors

Designer to choose colors to be used in the design.

Requirements
Must have
• Professional look including the company logo, need to have ability to request more information from us so needs a inquiries page, seperate pages for the different offerings, data governance, report modelling, business intelligence implementation, data protection
Nice to have
• any website interaction, animation, etc
Should not have
• too many colours, too busy pages, must look professional

```html
<!DOCTYPE html>
<html lang="en">
<head>
<meta charset="utf-8">
<title>Harlowe Data Ltd</title>
<link href="https://fonts.googleapis.com/css2?family=Bebas+Neue&family=Roboto:wght@400;500;700&family=Roboto+Condensed:wght@400;700&display=swap" rel="stylesheet">
<style>
:root{
  --blue:#1f72c6;
  --blue-dark:#165ea8;
  --blue-soft:#3d8ad8;
  --ink:#222;
  --text:#555;
  --muted:#999;
  --light:#f0f0f0;
  --dark:#262626;
  --footer:#1b1b1b;
  --white:#fff;
}
*{margin:0;padding:0;box-sizing:border-box}
html,body{width:1200px;height:3197px;overflow:hidden}
body{position:relative;background:var(--white);font-family:'Roboto',sans-serif;color:var(--text);font-size:12px}

/* header */
.site-header{position:absolute;left:0;top:0;width:1200px;height:92px;background:var(--white)}
.top-links{position:absolute;right:160px;top:0;height:18px;background:#eee;border-radius:0 0 10px 10px;padding:0 20px;display:flex;gap:24px;align-items:center;font-size:10px;color:#444}
.top-links span::before{content:"";display:inline-block;width:7px;height:7px;background:#555;border-radius:2px;margin-right:5px}
.brand{position:absolute;left:160px;top:14px;display:flex;align-items:center;gap:10px}
.brand-mark{width:30px;height:30px;background:var(--blue)}
.brand-name{font-weight:700;font-size:22px;color:var(--blue)}
.main-nav{position:absolute;right:160px;top:52px;display:flex;gap:23px;font-size:11.5px;font-weight:500;color:#333}
.main-nav .active{color:var(--blue)}

/* hero */
.hero{position:absolute;left:0;top:92px;width:1200px;height:498px;background:linear-gradient(100deg,#5d6670 0%,#8b939b 30%,#3b4148 55%,#23282e 100%)}
.hero-tag{position:absolute;left:632px;top:250px;background:var(--blue);color:#fff;font-family:'Roboto Condensed',sans-serif;font-weight:700;font-size:17px;padding:7px 14px}
.hero-title{position:absolute;left:632px;top:288px;background:#fff;color:#111;font-family:'Roboto Condensed',sans-serif;font-weight:700;font-size:27px;padding:6px 14px}

/* services band */
.services{position:absolute;left:0;top:590px;width:1200px;height:336px;background:linear-gradient(180deg,var(--blue) 0%,var(--blue-dark) 100%)}
.service-card{position:absolute;top:38px;width:210px;height:258px;border:2px solid rgba(255,255,255,.45);text-align:center;color:#fff;padding-top:30px}
.service-icon{width:76px;height:76px;border-radius:50%;background:rgba(255,255,255,.25);margin:0 auto;display:flex;align-items:center;justify-content:center}
.service-card h3{font-family:'Roboto Condensed',sans-serif;font-size:13px;font-weight:700;margin:26px 16px 10px;line-height:1.2;text-transform:uppercase}
.service-card p{font-size:10px;line-height:1.4;color:rgba(255,255,255,.65);padding:0 18px}
.btn-outline-light{display:inline-block;margin-top:16px;border:1px solid rgba(255,255,255,.8);color:#fff;font-size:9px;padding:6px 12px}

/* welcome */
.welcome{position:absolute;left:0;top:926px;width:1200px;height:364px;text-align:center}
.welcome h1{position:absolute;left:0;right:0;top:50px;font-family:'Bebas Neue',sans-serif;font-weight:400;font-size:38px;color:var(--ink);letter-spacing:.5px}
.welcome .sub{position:absolute;left:0;right:0;top:96px;font-size:11px;color:var(--muted)}
.divider{position:absolute;left:160px;width:880px;top:144px;height:1px;background:#ddd}
.divider-mark{position:absolute;left:584px;top:122px;width:32px;height:32px;background:#fff;display:flex;align-items:center;justify-content:center}
.divider-mark i{width:20px;height:20px;background:var(--blue)}
.welcome p{position:absolute;left:170px;width:860px;top:178px;font-size:11px;line-height:1.6;color:#444}
.btn-outline-dark{display:inline-block;border:1px solid #999;color:#222;font-size:10px;font-weight:700;padding:10px 18px}
.welcome .btn-outline-dark{position:absolute;left:547px;top:280px}

/* who we are */
.who{position:absolute;left:0;top:1290px;width:1200px;height:308px;background:var(--light)}
.who-photo{position:absolute;left:0;top:0;width:597px;height:308px;background:linear-gradient(120deg,#2f4d7a 0%,#6d8fb8 45%,#1f2e44 100%)}
.who h2{position:absolute;left:636px;top:40px;font-family:'Bebas Neue',sans-serif;font-weight:400;font-size:32px;color:var(--ink)}
.who p{position:absolute;left:636px;top:88px;width:404px;font-size:11px;line-height:1.6;color:#444;text-align:justify}
.who .btn-outline-dark{position:absolute;left:636px;top:236px}

/* inquiries */
.inquiry{position:absolute;left:0;top:1598px;width:1200px;height:192px;background:linear-gradient(90deg,#2a2a2a 0%,#333 60%,#1e1e1e 100%)}
.field{position:absolute;width:190px;height:32px;background:#ddd;font-size:9px;color:#777;padding:10px}
.btn-blue{background:var(--blue);color:#fff;font-family:'Roboto Condensed',sans-serif;font-weight:700;font-size:12px;text-align:center}
.inquiry .btn-blue{position:absolute;left:160px;top:127px;width:190px;height:30px;line-height:30px}
.inquiry-text{position:absolute;right:160px;top:42px;text-align:right;color:#fff;font-family:'Roboto Condensed',sans-serif;font-weight:700}
.inquiry-text .small{font-size:14px;margin-top:14px}
.inquiry-text .big{font-size:32px;line-height:1}

/* why choose */
.why{position:absolute;left:0;top:1790px;width:1200px;height:440px}
.why h2{position:absolute;left:0;right:0;top:40px;text-align:center;font-weight:700;font-size:29px;color:var(--ink)}
.why .rule{position:absolute;left:580px;top:86px;width:40px;height:3px;background:var(--blue)}
.reason{position:absolute;width:312px;font-size:10.5px;line-height:1.45;color:#444}
.reason h3{font-family:'Roboto Condensed',sans-serif;font-size:13px;font-weight:700;color:var(--ink);margin-bottom:4px}
.reason .more{display:block;margin-top:6px;font-size:9.5px;font-weight:700;color:var(--blue)}
.reason.left{text-align:right}
.num{position:absolute;width:84px;height:84px;border-radius:50%;background:var(--blue);border:4px solid #fff;box-shadow:0 0 0 3px var(--blue);color:#fff;font-size:31px;font-weight:500;display:flex;align-items:center;justify-content:center}

/* reach band */
.reach{position:absolute;left:0;top:2230px;width:1200px;height:246px;background:linear-gradient(90deg,#1a68b8 0%,#2b7ccc 50%,#1c6dbd 100%);text-align:center;color:#fff}
.reach h2{position:absolute;left:0;right:0;top:62px;font-family:'Roboto Condensed',sans-serif;font-weight:700;font-size:27px}
.reach p{position:absolute;left:0;right:0;top:104px;font-size:12px;color:rgba(255,255,255,.85)}
.btn-dark{position:absolute;left:541px;top:155px;width:118px;height:38px;line-height:38px;background:#1c1c1c;color:#fff;font-size:12px;font-weight:700}

/* clients */
.clients{position:absolute;left:0;top:2476px;width:1200px;height:330px}
.clients h2{position:absolute;left:0;right:0;top:40px;text-align:center;font-family:'Roboto Condensed',sans-serif;font-weight:700;font-size:25px;color:var(--ink)}
.clients h2 em{font-style:normal;color:var(--blue)}
.clients .rule{position:absolute;left:580px;top:80px;width:40px;height:3px;background:var(--blue)}
.client-photo{position:absolute;top:127px;width:220px;height:145px}
.client{position:absolute;top:135px;width:200px;font-size:10.5px;line-height:1.45;color:#444}
.client h3{font-weight:500;font-size:19px;color:var(--ink)}
.client .role{font-size:9.5px;color:var(--blue);margin:2px 0 8px}

/* newsletter */
.newsletter{position:absolute;left:0;top:2806px;width:1200px;height:199px;background:var(--light);text-align:center}
.newsletter h2{position:absolute;left:0;right:0;top:28px;font-family:'Roboto Condensed',sans-serif;font-weight:700;font-size:25px;color:var(--ink)}
.newsletter .sub{position:absolute;left:0;right:0;top:80px;font-size:10px;color:#555}
.input{position:absolute;top:120px;height:32px;background:#fff;border:1px solid #ddd;font-size:9.5px;color:#999;padding:10px;text-align:left}
.newsletter .btn-blue{position:absolute;left:877px;top:120px;width:160px;height:32px;line-height:32px}

/* footer */
.site-footer{position:absolute;left:0;top:3005px;width:1200px;height:147px;background:var(--footer);color:#bbb}
.foot-col{position:absolute;top:38px;font-size:11px;line-height:1.55}
.foot-col h4{color:#fff;font-family:'Roboto Condensed',sans-serif;font-size:13px;font-weight:700;margin-bottom:20px;display:flex;align-items:center;gap:8px}
.foot-col h4 svg{flex:none}
.bottom-bar{position:absolute;left:0;top:3152px;width:1200px;height:45px;background:var(--blue)}
.foot-nav{position:absolute;left:160px;top:15px;display:flex;gap:14px;font-size:10.5px;color:#fff}
.social{position:absolute;right:162px;top:10px;display:flex;gap:9px}
.social i{width:21px;height:21px;border-radius:50%;border:1.5px solid #fff}
</style>
</head>
<body>

<header class="site-header">
  <div class="top-links"><span>Home</span><span>Login</span><span>Register</span></div>
  <div class="brand"><div class="brand-mark"></div><div class="brand-name">Harlowe Data Ltd</div></div>
  <nav class="main-nav">
    <span class="active">HOME</span><span>ABOUT US</span><span>SERVICES</span><span>DATA</span><span>FEATURES</span><span>BLOG</span><span>PARTNERS</span><span>CONTACT US</span>
  </nav>
</header>

<section class="hero" role="img" aria-label="Photo of two businessmen shaking hands in a server room">
  <div class="hero-tag">WE ARE SPECIALISTS IN DATA</div>
  <div class="hero-title">OVER 25 YEARS OF EXPERIENCE</div>
</section>

<section class="services">
  <div class="service-card" style="left:162px">
    <div class="service-icon"><svg width="36" height="36" viewBox="0 0 36 36" fill="#fff"><rect x="5" y="6" width="7" height="24"/><rect x="14" y="6" width="7" height="24"/><rect x="24" y="8" width="7" height="22" transform="rotate(-12 27 19)"/></svg></div>
    <h3>Data Governance</h3>
    <p>Lorem Ipsum is simply dummy text industry's standard dummy text ever printer took</p>
    <span class="btn-outline-light">READ MORE ➔</span>
  </div>
  <div class="service-card" style="left:384px">
    <div class="service-icon"><svg width="36" height="36" viewBox="0 0 36 36" fill="#fff"><rect x="4" y="7" width="28" height="22" rx="2"/><rect x="8" y="11" width="9" height="7" fill="#3d8ad8"/><rect x="19" y="11" width="9" height="2" fill="#3d8ad8"/><rect x="19" y="15" width="9" height="2" fill="#3d8ad8"/><rect x="8" y="21" width="20" height="2" fill="#3d8ad8"/></svg></div>
    <h3>Report Modelling</h3>
    <p>Lorem Ipsum is simply dummy text industry's standard dummy text ever printer took</p>
    <span class="btn-outline-light">READ MORE ➔</span>
  </div>
  <div class="service-card" style="left:605px">
    <div class="service-icon"><svg width="36" height="36" viewBox="0 0 36 36" fill="#fff"><rect x="6" y="22" width="5" height="9"/><rect x="13" y="18" width="5" height="13"/><rect x="20" y="14" width="5" height="17"/><rect x="27" y="10" width="5" height="21"/><path d="M5 17 L14 10 L20 13 L29 5" stroke="#fff" stroke-width="2.5" fill="none"/></svg></div>
    <h3>Business Intelligence Implementation</h3>
    <p>Lorem Ipsum is simply dummy text industry's standard dummy text ever printer took</p>
    <span class="btn-outline-light">READ MORE ➔</span>
  </div>
  <div class="service-card" style="left:826px">
    <div class="service-icon"><svg width="36" height="36" viewBox="0 0 36 36" fill="#fff"><ellipse cx="16" cy="8" rx="11" ry="4"/><rect x="5" y="11" width="22" height="6" rx="3"/><rect x="5" y="19" width="22" height="6" rx="3"/><rect x="20" y="22" width="12" height="10" rx="1"/><path d="M23 22 v-3 a3 3 0 0 1 6 0 v3" stroke="#fff" stroke-width="2" fill="none"/></svg></div>
    <h3>Data Protection</h3>
    <p>Lorem Ipsum is simply dummy text industry's standard dummy text ever printer took</p>
    <span class="btn-outline-light">READ MORE ➔</span>
  </div>
</section>

<section class="welcome">
  <h1>WELCOME TO HARLOWE DATA LTD</h1>
  <div class="sub">Lorem Ipsum is simply dummy text typesetting industry</div>
  <div class="divider"></div>
  <div class="divider-mark"><i></i></div>
  <p>Lorem Ipsum is simply dummy text of the printing and typesetting industry. Lorem Ipsum has been the industry's standard dummy text ever since the 1500s, when an unknown printer took a galley of type and scrambled it to make a type specimen book. It has survived not only five centuries, but also the leap into electronic typesetting, remaining essentially unchanged. It was popularised in the 1960s with the release of transfer sheets containing Lorem Ipsum passages, and more recently with desktop publishing software like page layout tools including versions of Lorem Ipsum.Lorem Ipsum is simply dummy text</p>
  <span class="btn-outline-dark">READ MORE ➔</span>
</section>

<section class="who">
  <div class="who-photo" role="img" aria-label="Photo of two engineers checking server racks with a laptop"></div>
  <h2>WHO WE ARE</h2>
  <p>Lorem Ipsum is simply dummy text of the printing and typesetting industry. Lorem Ipsum has been the industry's standard dummy text ever since the 1500s, when an unknown printer took a galley of type and scrambled it to make a type specimen release publishing software like page layout tools including versions of Lorem Ipsum.Lorem Ipsum is simply dummy text of the printing and typesetting industry. specimen book. It has survived not only five centuries, but also the leap into electronic Ipsum.Lorem Ipsum is simply dummy text of the printing book.</p>
  <span class="btn-outline-dark">READ MORE ➔</span>
</section>

<section class="inquiry">
  <div class="field" style="left:160px;top:43px">Name / Company Name</div>
  <div class="field" style="left:357px;top:43px">Email</div>
  <div class="field" style="left:554px;top:43px">Phone Number</div>
  <div class="field" style="left:160px;top:83px">Number Of Employees</div>
  <div class="field" style="left:357px;top:83px">Number Of Outgoing Invoice</div>
  <div class="field" style="left:554px;top:83px">Number Of Incoming Invoice</div>
  <div class="btn-blue">GET A FREE QUOTE ⟶</div>
  <div class="inquiry-text">
    <svg width="56" height="44" viewBox="0 0 56 44" fill="#fff"><path d="M4 4h20v20c0 10-6 16-16 18l-2-5c6-2 8-6 8-11H4z"/><path d="M32 4h20v20c0 10-6 16-16 18l-2-5c6-2 8-6 8-11H32z"/></svg>
    <div class="small">GET INQUIRIES</div>
    <div class="big">FOR OUR SERVICES</div>
  </div>
</section>

<section class="why">
  <h2>WHY CHOOSE HARLOWE DATA LTD?</h2>
  <div class="rule"></div>
  <div class="reason left" style="left:163px;top:146px"><h3>PROVEN RECORD OF RESULTS</h3>Lorem Ipsum is simply dummy text of the printing and typesetting industry. Lorem Ipsum has been the industry's standard dummy text ever since the 1500s, when an unknown printer took a galley more recently with desktop publishing software like layout tools<span class="more">READ MORE ⟶</span></div>
  <div class="num" style="left:494px;top:141px">01</div>
  <div class="num" style="left:617px;top:141px">02</div>
  <div class="reason" style="left:722px;top:146px"><h3>YEARS OF EXPERIENCE</h3>Lorem Ipsum is simply dummy text of the printing and typesetting industry. Lorem Ipsum has been the industry's standard dummy text ever since the 1500s, when an unknown printer took a galley more recently with desktop publishing software like layout tools<span class="more">READ MORE ⟶</span></div>
  <div class="reason left" style="left:163px;top:286px"><h3>STRATEGIC AND AGGRESSIVE</h3>Lorem Ipsum is simply dummy text of the printing and typesetting industry. Lorem Ipsum has been the industry's standard dummy text ever since the 1500s, when an unknown printer took a galley more recently with desktop publishing software like layout tools<span class="more">READ MORE ⟶</span></div>
  <div class="num" style="left:494px;top:282px">03</div>
  <div class="num" style="left:617px;top:282px">04</div>
  <div class="reason" style="left:722px;top:286px"><h3>SMALL TO MEDIUM ENTERPRISE</h3>Lorem Ipsum is simply dummy text of the printing and typesetting industry. Lorem Ipsum has been the industry's standard dummy text ever since the 1500s, when an unknown printer took a galley more recently with desktop publishing software like layout tools<span class="more">READ MORE ⟶</span></div>
</section>

<section class="reach">
  <h2>REACH YOUR POTENTIAL FASTER AND WITH EASE</h2>
  <p>We will take care of your comapany data and administrative services and take the load off you.</p>
  <div class="btn-dark">GET A QUOTE</div>
</section>

<section class="clients">
  <h2>CLIENTS THAT <em>TRUST</em> US</h2>
  <div class="rule"></div>
  <div class="client-photo" style="left:160px;background:linear-gradient(135deg,#c9cfd6,#8e9aa6)" role="img" aria-label="Photo of a team meeting around a laptop"></div>
  <div class="client" style="left:405px"><h3>OWEN MARSH</h3><div class="role">Ferrow Ltd CEO</div>Lorem Ipsum is simply dummy text printing and typesetting industry. Lorem Ipsum has been the industry's standard dummy text to make a type specimen book.</div>
  <div class="client-photo" style="left:615px;background:linear-gradient(135deg,#d7d5cf,#9a9890)" role="img" aria-label="Photo of a businesswoman working at a laptop in an office"></div>
  <div class="client" style="left:852px"><h3>CLARA BENTON</h3><div class="role">Brightlane Co CEO</div>Lorem Ipsum is simply dummy text printing and typesetting industry. Lorem Ipsum has been the industry's standard dummy text to make a type specimen book.</div>
</section>

<section class="newsletter">
  <h2>SUBSCRIBE TO OUR NEWSLETTER</h2>
  <div class="sub">If you want to receive monthly updates from us just pop your email in the box.</div>
  <div class="input" style="left:160px;width:352px">Enter your name</div>
  <div class="input" style="left:525px;width:340px">Enter your email address</div>
  <div class="btn-blue">SUBSCRIBE NOW</div>
</section>

<footer class="site-footer">
  <div class="foot-col" style="left:160px">
    <h4><svg width="11" height="15" viewBox="0 0 11 15"><path d="M5.5 0a5.5 5.5 0 0 0-5.5 5.5C0 10 5.5 15 5.5 15S11 10 11 5.5A5.5 5.5 0 0 0 5.5 0z" fill="#fff"/><circle cx="5.5" cy="5.5" r="2" fill="#1b1b1b"/></svg>OUR ADDRESS</h4>
    14 Kestrel Row<br>Leeds, United Kingdom
  </div>
  <div class="foot-col" style="left:527px">
    <h4><svg width="15" height="11" viewBox="0 0 15 11"><rect x=".5" y=".5" width="14" height="10" fill="none" stroke="#fff"/><path d="M.5 .5l7 6 7-6" fill="none" stroke="#fff"/></svg>CONTACT US</h4>
    +44 113 496 0321<br>hello@harlowedata.co.uk
  </div>
  <div class="foot-col" style="left:878px;text-align:right;width:162px">
    <h4><svg width="14" height="14" viewBox="0 0 14 14"><circle cx="7" cy="7" r="6" fill="none" stroke="#fff" stroke-width="1.5"/><path d="M7 3.5V7l2.5 1.5" stroke="#fff" stroke-width="1.5" fill="none"/></svg>OFFICE HOURS</h4>
    Monday to Friday: 8:00 - 17:00<br>Saturday, Sunday: 9:00 - 14:00
  </div>
</footer>

<div class="bottom-bar">
  <nav class="foot-nav"><span>About Us</span><span>Services</span><span>Data</span><span>Features</span><span>Blog</span><span>Partners</span><span>Contact us</span></nav>
  <div class="social"><i></i><i></i><i></i><i></i><i></i></div>
</div>

</body>
</html>
```